Dental office Stationary & Business card
Marlowe Pines Dental LLC
Dental office Stationary & Business card - Health
Creative Brief
Professional
Implants- Cosmetics- Generals- Braces
2815 Quarry Hollow Pkwy. Unit 3407 Norcross, GA 30071
mpdoffice@tinmail.example
www.marlowepinesdental.example
We would like designers to include for us the following: business card, letter head, envelope label, and e-signature template. logo design files can be downloaded below: https://www.filecrate.example/s/q8zrt3mw1xk5pa/Modern%20logo%20for%20a%20dental%20office.zip
Please have this content in the back of the card. "Your next appointment is on ____________ at _______ AM/PM

```html
<!DOCTYPE html>
<html lang="en">
<head>
<meta charset="utf-8">
<title>Marlowe Pines Dental – Business Card</title>
<link rel="stylesheet" href="https://fonts.googleapis.com/css2?family=Open+Sans:wght@400;600&display=swap">
<style>
  :root {
    --page-bg: #ece8e4;
    --card-white: #ffffff;
    --brown-deep: #6a3824;
    --brown-band: #93654a;
    --brown-text: #5e3020;
    --ink-light: #ffffff;
  }
  html, body {
    margin: 0;
    width: 1200px;
    height: 958px;
    overflow: hidden;
    background: var(--page-bg);
    font-family: "Open Sans", Arial, sans-serif;
  }
  .business-card {
    position: absolute;
    left: 80px;
    top: 182px;
    width: 1040px;
    height: 594px;
    border-radius: 6px;
    overflow: hidden;
    box-shadow: 0 10px 30px rgba(60, 35, 20, 0.25);
    background: var(--brown-deep);
  }
  .card-shapes {
    position: absolute;
    inset: 0;
  }
  .brand-lockup {
    position: absolute;
    left: 60px;
    top: 215px;
    width: 400px;
    text-align: center;
    color: var(--brown-text);
  }
  .brand-mark {
    width: 64px;
    height: 64px;
    margin: 0 auto 14px;
    border-radius: 50%;
    background: var(--brown-text);
  }
  .brand-name {
    font-size: 34px;
    font-weight: 600;
    letter-spacing: 1px;
    line-height: 1.15;
  }
  .brand-doctor {
    margin-top: 8px;
    font-size: 18px;
    font-weight: 600;
    letter-spacing: 1px;
  }
  .contact-block {
    position: absolute;
    right: 60px;
    top: 56px;
    text-align: right;
    color: var(--ink-light);
  }
  .holder-name {
    font-size: 30px;
    font-weight: 600;
    line-height: 1.2;
  }
  .holder-role {
    font-size: 24px;
    margin-bottom: 58px;
  }
  .contact-line {
    font-size: 22px;
    line-height: 1.55;
    display: flex;
    justify-content: flex-end;
    align-items: center;
    gap: 10px;
  }
  .contact-icon {
    width: 20px;
    height: 20px;
    fill: var(--ink-light);
    flex: none;
  }
</style>
</head>
<body>
  <div class="business-card">
    <svg class="card-shapes" viewBox="0 0 1040 594" preserveAspectRatio="none">
      <path fill="var(--brown-band)" d="M0 0 H490 C610 120 610 420 470 594 H0 Z"/>
      <path fill="var(--card-white)" d="M0 0 H440 C565 130 565 420 420 594 H0 Z"/>
    </svg>

    <div class="brand-lockup">
      <div class="brand-mark"></div>
      <div class="brand-name">Marlowe Pines Dental</div>
      <div class="brand-doctor">Dr. Elin Marsh D.D.S</div>
    </div>

    <div class="contact-block">
      <div class="holder-name">Corin Halvard-Lee</div>
      <div class="holder-role">Consultant</div>
      <div class="contact-line">214.9th floor.Plaza</div>
      <div class="contact-line">Fernbank Road QRV</div>
      <div class="contact-line">012 555 0147
        <svg class="contact-icon" viewBox="0 0 24 24"><path d="M6.6 10.8a15.1 15.1 0 0 0 6.6 6.6l2.2-2.2a1 1 0 0 1 1-.25 11.4 11.4 0 0 0 3.6.6 1 1 0 0 1 1 1V20a1 1 0 0 1-1 1A17 17 0 0 1 3 4a1 1 0 0 1 1-1h3.5a1 1 0 0 1 1 1c0 1.25.2 2.45.6 3.6a1 1 0 0 1-.25 1z"/></svg>
      </div>
      <div class="contact-line">012 555 0148
        <svg class="contact-icon" viewBox="0 0 24 24"><path d="M6 3h10v5H6z M4 9h16a2 2 0 0 1 2 2v6h-4v4H6v-4H2v-6a2 2 0 0 1 2-2z M8 15v4h8v-4z"/></svg>
      </div>
      <div class="contact-line">mpdoffice@tinmail.example
        <svg class="contact-icon" viewBox="0 0 24 24"><path d="M2 5h20v14H2z M3.5 6.5 12 13l8.5-6.5" stroke="var(--brown-deep)" stroke-width="1.5"/></svg>
      </div>
      <div class="contact-line">www.marlowepinesdental.example</div>
    </div>
  </div>
</body>
</html>
```